Webbanner-Design holvira.at Webshop
Zielgruppe
Onlineshop für Haus + Garten
holvira.at
Aufgabenstellung
Benötigt wird ein neues Banner-Set
ein Allgemeines - warum bei holvira.at einkaufen
- günstige Preise durch Direktbezug ohne Zwischenhandel
- alle Artikel vorrätig - schnelle Lieferung
- Sichere Kaufabwicklung - Lumena Kauf
- Fachberatung und Service durch geschultes Peronal
sowie Banner für jede Hauptkategorie

```html
<!DOCTYPE html>
<html lang="de">
<head>
<meta charset="utf-8">
<title>holvira.at – Bad, Pool und mehr</title>
<link href="https://fonts.googleapis.com/css2?family=Open+Sans:wght@400;600;700;800&display=swap" rel="stylesheet">
<style>
  :root {
    --brand-gold: #c9a75f;
    --brand-navy: #1f3f86;
    --banner-blue-a: #213f8a;
    --banner-blue-b: #2a5da8;
    --link-blue: #3a8fd6;
    --nav-text: #555a60;
    --nav-band-top: #ffffff;
    --nav-band-bottom: #e6e7e8;
    --badge-navy: #1d2f52;
    --dark-button: #3c3c3c;
    --field-border: #c8c8c8;
    --white: #ffffff;
  }
  * { box-sizing: border-box; margin: 0; padding: 0; }
  html, body { width: 1200px; height: 745px; overflow: hidden; }
  body {
    position: relative;
    font-family: "Open Sans", Arial, sans-serif;
    background: var(--white);
  }
  .header { position: absolute; left: 0; top: 0; width: 1200px; height: 110px; background: var(--white); }
  .logo {
    position: absolute; left: 56px; top: 38px;
    display: flex; align-items: center; gap: 7px;
    font-weight: 800; font-size: 27px; color: var(--brand-gold); letter-spacing: -0.5px;
  }
  .logo-square { width: 20px; height: 20px; background: var(--brand-navy); }
  .seal-badge {
    position: absolute; left: 342px; top: 36px; width: 52px; height: 52px;
    border-radius: 50%; background: var(--badge-navy);
    border: 3px solid var(--brand-gold);
  }
  .service-links {
    position: absolute; left: 892px; top: 15px;
    display: flex; font-size: 12px; color: var(--link-blue);
  }
  .service-links span { padding: 0 7px; border-left: 1px solid #cfd4da; }
  .service-links span:first-child { border-left: none; padding-left: 0; }
  .lang-button {
    position: absolute; left: 1069px; top: 13px; width: 77px; height: 21px;
    background: var(--dark-button); border-radius: 3px;
    color: var(--white); font-size: 12px; line-height: 21px; padding-left: 19px;
  }
  .lang-button::before {
    content: ""; position: absolute; left: 6px; top: 6px; width: 9px; height: 9px;
    border: 1px solid var(--white); border-radius: 1px;
  }
  .search {
    position: absolute; left: 676px; top: 49px; width: 242px; height: 36px;
    border: 1px solid var(--field-border); border-radius: 3px; background: var(--white);
  }
  .search-placeholder { position: absolute; left: 12px; top: 8px; font-size: 14px; color: #999; }
  .search-button {
    position: absolute; right: 0; top: 0; width: 40px; height: 34px;
    background: #f2f2f2; border-left: 1px solid var(--field-border);
    display: flex; align-items: center; justify-content: center;
  }
  .account, .cart {
    position: absolute; top: 64px; font-size: 14.5px; color: var(--link-blue);
    display: flex; align-items: center; gap: 5px;
  }
  .account { left: 947px; }
  .cart { left: 1069px; }
  .main-nav {
    position: absolute; left: 0; top: 110px; width: 1200px; height: 61px;
    background: linear-gradient(var(--nav-band-top), var(--nav-band-bottom));
  }
  .main-nav span {
    position: absolute; top: 21px; font-size: 14px; color: var(--nav-text);
    display: flex; align-items: center; gap: 3px;
  }
  .caret { width: 0; height: 0; border-left: 3.5px solid transparent; border-right: 3.5px solid transparent; border-top: 4px solid var(--nav-text); }
  .stage-backdrop {
    position: absolute; left: 0; top: 171px; width: 1200px; height: 574px;
    background: linear-gradient(90deg, #7d9bab 0%, #b9cfd8 10%, #a9c6d1 50%, #6fa4b3 85%, #2f7f95 100%);
  }
  .slider-panel {
    position: absolute; left: 50px; top: 185px; width: 1100px; height: 549px;
    background: var(--white);
  }
  .banner { position: absolute; left: 23px; top: 22px; width: 1055px; height: 439px; }
  .banner-bg { position: absolute; left: 0; top: 0; }
  .banner-kicker {
    position: absolute; left: 38px; top: 34px; font-size: 16.5px; color: var(--white);
  }
  .banner-kicker b { font-weight: 700; }
  .banner-title {
    position: absolute; left: 37px; top: 78px; font-size: 37px; line-height: 41px;
    font-weight: 700; color: var(--white);
  }
  .banner-list { position: absolute; left: 38px; top: 182px; list-style: none; }
  .banner-list li {
    font-size: 23px; line-height: 28.5px; font-weight: 700; color: var(--white);
    display: flex; align-items: center; gap: 7px;
  }
  .bullet-chevron { flex: none; width: 14px; height: 16px; display: block; }
  .cta {
    position: absolute; left: 38px; top: 359px; width: 155px; height: 44px;
    background: var(--brand-gold); color: var(--white);
    font-size: 12px; font-weight: 700; text-align: center; line-height: 44px;
  }
  .price-seal {
    position: absolute; left: 889px; top: 274px; width: 128px; height: 128px;
    border-radius: 50%; background: var(--brand-gold); color: var(--white);
    text-align: center; font-weight: 700; padding-top: 38px;
  }
  .price-seal small { display: block; font-size: 11.5px; line-height: 17.5px; }
  .price-seal strong { display: block; font-size: 25px; line-height: 32px; }
  .slider-dots {
    position: absolute; left: 474px; top: 502px; display: flex; gap: 19px; align-items: center;
  }
  .slider-dots i { width: 6px; height: 6px; border-radius: 50%; background: #444; display: block; }
  .slider-dots i.active { width: 10px; height: 10px; background: transparent; border: 2px solid #444; margin: 0 -2px; }
</style>
</head>
<body>
  <header class="header">
    <div class="logo"><span class="logo-square"></span>holvira.at</div>
    <div class="seal-badge" aria-label="Lumena Kauf Gütesiegel"></div>
    <nav class="service-links"><span>News</span><span>Kontakt</span><span>Links</span></nav>
    <div class="lang-button">Deutsch ▾</div>
    <div class="search">
      <span class="search-placeholder">Suchen</span>
      <span class="search-button">
        <svg width="16" height="16" viewBox="0 0 16 16"><circle cx="6.5" cy="6.5" r="5" fill="none" stroke="#2a6fb5" stroke-width="2"/><line x1="10.2" y1="10.2" x2="14.5" y2="14.5" stroke="#2a6fb5" stroke-width="2.4" stroke-linecap="round"/></svg>
      </span>
    </div>
    <div class="account">
      <svg width="11" height="12" viewBox="0 0 11 12"><circle cx="5.5" cy="3" r="3" fill="#3a8fd6"/><path d="M0 12 Q0 6.5 5.5 6.5 Q11 6.5 11 12Z" fill="#3a8fd6"/></svg>
      Anmelden <span class="caret" style="border-top-color:#3a8fd6"></span>
    </div>
    <div class="cart">
      <svg width="13" height="12" viewBox="0 0 13 12"><path d="M0 1h2.5l1.8 7h7l1.5-5.5H3.5" fill="none" stroke="#3a8fd6" stroke-width="1.6"/><rect x="3.6" y="3" width="8.2" height="4.4" fill="#3a8fd6"/><circle cx="5" cy="10.5" r="1.3" fill="#3a8fd6"/><circle cx="10" cy="10.5" r="1.3" fill="#3a8fd6"/></svg>
      0,00 € <span class="caret" style="border-top-color:#3a8fd6"></span>
    </div>
  </header>

  <nav class="main-nav">
    <span style="left:64px">Badezimmer<i class="caret"></i></span>
    <span style="left:183px">Schwimmbecken<i class="caret"></i></span>
    <span style="left:328px">Schwimmbadzubehör<i class="caret"></i></span>
    <span style="left:505px">Sauna</span>
    <span style="left:572px">Heizung, Solar, Klima<i class="caret"></i></span>
    <span style="left:743px">Garten<i class="caret"></i></span>
    <span style="left:826px">Kabelkanal</span>
    <span style="left:923px">Whirlpoolzubehör<i class="caret"></i></span>
  </nav>

  <div class="stage-backdrop" role="img" aria-label="Unscharfes Poolwasser als Hintergrund"></div>

  <section class="slider-panel">
    <div class="banner">
      <svg class="banner-bg" width="1055" height="439" viewBox="0 0 1055 439">
        <defs>
          <linearGradient id="bannerBlue" x1="0" y1="0" x2="1" y2="1">
            <stop offset="0" stop-color="#213f8a"/>
            <stop offset="1" stop-color="#2a60aa"/>
          </linearGradient>
          <linearGradient id="poolScene" x1="0" y1="0" x2="0" y2="1">
            <stop offset="0" stop-color="#3f6d34"/>
            <stop offset="0.18" stop-color="#6f8a55"/>
            <stop offset="0.28" stop-color="#d6cdbd"/>
            <stop offset="0.42" stop-color="#3d8ed2"/>
            <stop offset="0.78" stop-color="#2d82cf"/>
            <stop offset="0.9" stop-color="#cfc5b4"/>
            <stop offset="1" stop-color="#ddd3c3"/>
          </linearGradient>
        </defs>
        <rect width="1055" height="439" fill="url(#bannerBlue)"/>
        <path d="M448 0 H1055 V439 H464 Q340 219 448 0Z" fill="#c9a75f"/>
        <g role="img" aria-label="Foto eines runden Schwimmbeckens mit Pflanzen im Garten">
          <path d="M491 0 H1055 V439 H479 Q363 219 491 0Z" fill="url(#poolScene)"/>
        </g>
      </svg>
      <p class="banner-kicker"><b>IHR FACHMANN</b> FÜR BAD, POOL UND MEHR</p>
      <h1 class="banner-title">IHR EIGENES<br>SCHWIMMBECKEN</h1>
      <ul class="banner-list">
        <li><svg class="bullet-chevron" viewBox="0 0 14 16"><path d="M1 0h6l7 8-7 8H1l7-8z" fill="#c9a75f"/></svg>STAHLMANTELBECKEN</li>
        <li><svg class="bullet-chevron" viewBox="0 0 14 16"><path d="M1 0h6l7 8-7 8H1l7-8z" fill="#c9a75f"/></svg>SYSTEMSTEINBECKEN</li>
        <li><svg class="bullet-chevron" viewBox="0 0 14 16"><path d="M1 0h6l7 8-7 8H1l7-8z" fill="#c9a75f"/></svg>AUFSTELLBECKEN UVM.</li>
      </ul>
      <div class="cta">ENTDECKEN</div>
      <div class="price-seal"><small>HOCHWERTIGE<br>BECKEN AB NUR</small><strong>59,99€</strong></div>
    </div>
    <div class="slider-dots"><i></i><i></i><i></i><i></i><i class="active"></i><i></i><i></i></div>
  </section>
</body>
</html>
```